Banner Ad for online campaigns needed

For our company (Flight simulator experience) we are looking for a banner that will be used for our online marketing campaigns.
Skyvane Flight Simulators allow anyone from six years old to experience flying a large passenger jet, accompanied by a trained co-pilot.

---
The idea behind the project:

It's about what our instructors favorite landings or airports are and thus inspire our customers to try those airports and indeed a skyvane flight.

So it could be mira. Instructor. Having our instructor ID displayed.
And then something like.
Fulfil your dream of being a pilot for a day.
My favorite airport is in Hong Kong. Challenging, thrilling and unexpected landing!
For this experience or for a choice of 24000 airports book your skyvane experience today. Skyvane is the ultimate gift for someone special!

would be great if some text is hand written - "so the pilot really says that.."
----
Need two sizes /same motive/
Size:
Square: 250 x 250
Wide skyscraper: 160 x 600
***
looking for a longterm cooperation
***
Attached:
our logo, + some ideas, picture of our ID
DO NOT use this picture and name in the proposal

Target Market(s)

the main audiance are woman who are looking for gifts for their husbands/brothers. they are looking for something extra and not usual.
they want to fullfill their dreams.

Industry/Entity Type

Marketing

Requirements
Must have
• DO NOT use the attached picture and name in the proposal in your final submission!, bring your own ideas

must be super clear that we are a flight simulator experience

Logo/font requirements:
red: PANTONE 485 U | C CMYK 0 | 100 | 100 | 0 RGB 226 | 0 | 26 HTML #E2001A RAL 3020
black: PANTONE PROCESS BLACK U | C CMYK 0 | 0 | 0 | 100 RGB 0 | 0 | 0 HTML #000000 RAL 9005

FUTURA T LIGHT, URW, NORMAL

Should not have
• no game related notes

```html
<!DOCTYPE html>
<html lang="en">
<head>
<meta charset="utf-8">
<title>Skyvane Flight Simulators – Banner Set</title>
<link rel="stylesheet" href="https://fonts.googleapis.com/css2?family=Oswald:wght@400;500;600&family=Roboto:wght@400;500&display=swap">
<style>
  :root{
    --stage:#2a2a2a;
    --brand-red:#e2001a;
    --red-deep:#8f0010;
    --red-mid:#c0001a;
    --gold:#ffd200;
    --white:#ffffff;
    --ink:#222222;
    --grey-edge:#bdbdbd;
    --photo-dark:#1c1f26;
    --photo-mid:#3c4250;
    --sky:#7fb2d8;
  }
  *{margin:0;padding:0;box-sizing:border-box}
  html,body{width:1200px;height:961px;overflow:hidden;background:var(--stage)}
  .stage{position:relative;width:1200px;height:961px}
  .banner{position:absolute;background:var(--white);overflow:hidden;box-shadow:0 6px 18px rgba(0,0,0,.55)}
  .banner--sky{left:232px;top:75px;width:222px;height:828px}
  .banner--square{left:567px;top:339px;width:446px;height:371px}

  .brand{position:absolute;display:flex;flex-direction:column}
  .brand__row{display:flex;align-items:center;gap:8px}
  .brand__name{font-family:"Oswald",sans-serif;font-weight:500;color:var(--brand-red);line-height:1;letter-spacing:.5px}
  .brand__dot{width:12px;height:12px;border-radius:50%;background:var(--brand-red)}
  .brand__tag{font-family:"Roboto",sans-serif;font-weight:500;color:var(--brand-red);font-size:10px;letter-spacing:.2px;margin-top:4px}

  .photo{position:absolute;background:
    linear-gradient(180deg,var(--photo-dark) 0%,var(--photo-mid) 28%,var(--sky) 32%,var(--sky) 40%,var(--photo-mid) 44%,var(--photo-dark) 100%)}

  .headline{position:absolute;left:0;right:0;text-align:center;font-family:"Oswald",sans-serif;color:var(--white);line-height:1.2}
  .headline__lead{font-weight:500;font-size:26px;letter-spacing:-.3px}
  .headline__hero{font-weight:500;color:var(--gold);font-size:33px;letter-spacing:-.5px;line-height:1.15}
  .headline__sub{font-weight:500;font-size:22px;letter-spacing:-.3px;line-height:1.2;margin-top:8px}

  .url{position:absolute;font-family:"Roboto",sans-serif;text-align:center}
  .cta{position:absolute;display:flex;align-items:center;justify-content:center;gap:8px;
    background:linear-gradient(180deg,#f2282f 0%,var(--brand-red) 45%,#a30010 100%);
    border-radius:8px;box-shadow:0 3px 5px rgba(0,0,0,.45);
    font-family:"Oswald",sans-serif;font-weight:500;color:var(--white);font-size:27px;letter-spacing:-.3px}
  .cta svg{width:24px;height:24px}
</style>
</head>
<body>
<div class="stage">

  <!-- Wide skyscraper -->
  <section class="banner banner--sky">
    <div class="brand" style="left:12px;top:34px">
      <div class="brand__row"><span class="brand__name" style="font-size:34px">SKYVANE</span><span class="brand__dot"></span></div>
      <span class="brand__tag">FLIGHT SIMULATOR EXPERIENCE</span>
    </div>
    <div class="photo" role="img" aria-label="Photo of a passenger jet flight simulator cockpit" style="left:0;top:113px;width:222px;height:300px"></div>
    <svg style="position:absolute;left:0;top:380px" width="222" height="325" viewBox="0 0 222 325">
      <defs><linearGradient id="skyRed" x1="0" y1="0" x2="0" y2="1">
        <stop offset="0" stop-color="#d4001a"/><stop offset=".45" stop-color="#9e0012"/><stop offset="1" stop-color="#b00015"/></linearGradient></defs>
      <path d="M0 60 Q110 10 222 0 L222 325 L0 325 Z" fill="var(--grey-edge)"/>
      <path d="M0 66 Q110 16 222 8 L222 325 L0 325 Z" fill="url(#skyRed)"/>
    </svg>
    <div class="headline" style="top:480px">
      <div class="headline__lead">Fulfil your husband's<br>dream to become a</div>
      <div class="headline__hero">PILOT FOR A DAY</div>
      <div class="headline__sub">He will be overjoyed<br>with our flight<br>simulator experience!</div>
    </div>
    <div class="url" style="left:0;right:0;top:719px;font-size:20px;color:var(--ink)">www.flyskyvane.com</div>
    <div class="cta" style="left:11px;top:753px;width:200px;height:57px">LEARN MORE
      <svg viewBox="0 0 24 24"><circle cx="12" cy="12" r="11" fill="#fff"/><path d="M6 10h6V6l7 6-7 6v-4H6z" fill="var(--brand-red)"/></svg>
    </div>
  </section>

  <!-- Square -->
  <section class="banner banner--square">
    <div class="photo" role="img" aria-label="Photo of a passenger jet flight simulator cockpit" style="left:0;top:0;width:240px;height:285px"></div>
    <svg style="position:absolute;left:180px;top:0" width="266" height="285" viewBox="0 0 266 285">
      <defs><linearGradient id="sqRed" x1="0" y1="0" x2="0" y2="1">
        <stop offset="0" stop-color="#d4001a"/><stop offset=".5" stop-color="#9e0012"/><stop offset="1" stop-color="#b80016"/></linearGradient></defs>
      <path d="M20 0 Q-15 140 45 285 L266 285 L266 0 Z" fill="var(--grey-edge)"/>
      <path d="M28 0 Q-6 140 53 285 L266 285 L266 0 Z" fill="url(#sqRed)"/>
    </svg>
    <div class="headline" style="left:225px;right:0;top:20px">
      <div class="headline__lead">Fulfil your husband's<br>dream to become a</div>
      <div class="headline__hero">PILOT FOR A DAY</div>
      <div class="headline__sub" style="margin-top:4px">He will be overjoyed<br>with our flight<br>simulator experience!</div>
    </div>
    <div class="url" style="left:225px;right:0;top:244px;font-size:20px;font-weight:500;color:var(--gold)">www.flyskyvane.com</div>
    <div class="brand" style="left:13px;top:310px">
      <div class="brand__row"><span class="brand__name" style="font-size:30px">SKYVANE</span><span class="brand__dot"></span></div>
      <span class="brand__tag">FLIGHT SIMULATOR EXPERIENCE</span>
    </div>
    <div class="cta" style="left:238px;top:301px;width:199px;height:55px">LEARN MORE
      <svg viewBox="0 0 24 24"><circle cx="12" cy="12" r="11" fill="#fff"/><path d="M6 10h6V6l7 6-7 6v-4H6z" fill="var(--brand-red)"/></svg>
    </div>
  </section>

</div>
</body>
</html>
```